Harold Vane Collective - Juvenile Skeletal Repair Agenda Framing Network

A 2-sided A4 leaflet to explain the research priorities in Children's Orthopaedic Surgery.
We would like this to be similar to that produced previously by the physiotherapists.

```html
<!DOCTYPE html>
<html lang="en">
<head>
<meta charset="utf-8">
<title>Our Top-10 Research Priorities</title>
<link href="https://fonts.googleapis.com/css2?family=EB+Garamond:wght@600&family=Roboto:ital,wght@0,400;0,500;0,700;0,900;1,500&display=swap" rel="stylesheet">
<style>
  :root {
    --backdrop: #e9e7e4;
    --paper: #f1f1f2;
    --brand-red: #c8102e;
    --ink: #1b1b1d;
    --band-black: #141416;
    --white: #ffffff;
  }
  html, body {
    margin: 0;
    width: 1200px;
    height: 1013px;
    overflow: hidden;
    background: var(--backdrop);
  }
  .leaflet {
    position: absolute;
    left: 260px;
    top: 26px;
    width: 679px;
    height: 960px;
    background: var(--paper);
    box-shadow: 0 6px 24px rgba(0,0,0,0.18);
    overflow: hidden;
  }
  .leaflet__title {
    position: absolute;
    top: 54px;
    left: 0;
    width: 100%;
    margin: 0;
    text-align: center;
    font-family: "EB Garamond", Georgia, serif;
    font-weight: 600;
    font-size: 29px;
    letter-spacing: 0.5px;
    color: var(--brand-red);
  }
  .priority-chain {
    position: absolute;
    left: 0;
    top: 0;
  }
  .priority-chain__number {
    font-family: "Roboto", Arial, sans-serif;
    font-weight: 900;
    font-size: 26px;
    fill: var(--white);
    text-anchor: middle;
    dominant-baseline: central;
  }
  .priority-list {
    list-style: none;
    margin: 0;
    padding: 0;
  }
  .priority {
    position: absolute;
    left: 125px;
    width: 489px;
    height: 69px;
    display: flex;
    align-items: center;
    font-family: "Roboto", Arial, sans-serif;
    font-weight: 500;
    font-size: 13px;
    line-height: 16.5px;
    color: var(--ink);
    text-align: justify;
    hyphens: auto;
  }
  .thanks-bar {
    position: absolute;
    left: 0;
    top: 851px;
    width: 100%;
    height: 34px;
    background: var(--band-black);
    color: var(--white);
    font-family: "Roboto", Arial, sans-serif;
    font-style: italic;
    font-weight: 500;
    font-size: 11.5px;
    line-height: 34px;
    text-align: center;
  }
  .credits {
    position: absolute;
    left: 0;
    top: 885px;
    width: 100%;
    height: 75px;
    background: var(--brand-red);
    color: var(--white);
    font-family: "Roboto", Arial, sans-serif;
  }
  .credits__heading {
    position: absolute;
    left: 45px;
    top: 20px;
    margin: 0;
    font-weight: 700;
    font-size: 28px;
  }
  .credits__list {
    position: absolute;
    left: 350px;
    top: 17px;
    margin: 0;
    padding: 0;
    list-style: none;
    font-weight: 500;
    font-size: 9.5px;
    line-height: 12px;
  }
</style>
</head>
<body>
<main class="leaflet">
  <h1 class="leaflet__title">OUR TOP-10 RESEARCH PRIORITIES</h1>

  <svg class="priority-chain" width="170" height="840" viewBox="0 0 170 840" aria-hidden="true">
    <line x1="86" y1="161" x2="86" y2="783" stroke="var(--band-black)" stroke-width="13"/>
    <g fill="var(--band-black)">
      <circle cx="86" cy="161" r="25"/><circle cx="86" cy="230.1" r="25"/><circle cx="86" cy="299.2" r="25"/>
      <circle cx="86" cy="368.3" r="25"/><circle cx="86" cy="437.4" r="25"/><circle cx="86" cy="506.6" r="25"/>
      <circle cx="86" cy="575.7" r="25"/><circle cx="86" cy="644.8" r="25"/><circle cx="86" cy="713.9" r="25"/>
      <circle cx="86" cy="783" r="25"/>
    </g>
    <g fill="var(--brand-red)">
      <circle cx="86" cy="161" r="21"/><circle cx="86" cy="230.1" r="21"/><circle cx="86" cy="299.2" r="21"/>
      <circle cx="86" cy="368.3" r="21"/><circle cx="86" cy="437.4" r="21"/><circle cx="86" cy="506.6" r="21"/>
      <circle cx="86" cy="575.7" r="21"/><circle cx="86" cy="644.8" r="21"/><circle cx="86" cy="713.9" r="21"/>
      <circle cx="86" cy="783" r="21"/>
    </g>
    <text class="priority-chain__number" x="86" y="161">1</text>
    <text class="priority-chain__number" x="86" y="230.1">2</text>
    <text class="priority-chain__number" x="86" y="299.2">3</text>
    <text class="priority-chain__number" x="86" y="368.3">4</text>
    <text class="priority-chain__number" x="86" y="437.4">5</text>
    <text class="priority-chain__number" x="86" y="506.6">6</text>
    <text class="priority-chain__number" x="86" y="575.7">7</text>
    <text class="priority-chain__number" x="86" y="644.8">8</text>
    <text class="priority-chain__number" x="86" y="713.9">9</text>
    <text class="priority-chain__number" x="85" y="783" style="letter-spacing:-2px">10</text>
  </svg>

  <ol class="priority-list">
    <li class="priority" style="top:126.5px">What are the best ways to measure the outcome following lower limb orthopaedic surgery in children?</li>
    <li class="priority" style="top:195.6px">Following orthopaedic surgery to the lower limbs, what should children’s rehabilitation include, how long is it expected to last and how does it affect the result of treatment?</li>
    <li class="priority" style="top:264.7px">What is the short-term and long-term clinical and cost effectiveness of orthopaedic lower limb surgery (including best timing and technique) for children with Cerebral Palsy who can walk?</li>
    <li class="priority" style="top:333.8px">What are the short term and long term outcomes of surgery compared to non-surgical care in the treatment of Perthes disease of the hip?</li>
    <li class="priority" style="top:402.9px">What is the clinical and cost effectiveness of pre-operative rehabilitation in children presenting with lower limb orthopaedic conditions?</li>
    <li class="priority" style="top:472.1px">What is the short-term and long-term clinical and cost effectiveness of Selective Dorsal Rhizotomy (SDR) in children with Cerebral Palsy who can walk?</li>
    <li class="priority" style="top:541.2px">Can surveillance and non-surgical treatment (e.g. physiotherapy, botulinum toxin injections, functional electrical stimulation, orthotics, casting) prevent the development of deformity requiring surgery in children with Cerebral Palsy?</li>
    <li class="priority" style="top:610.3px">What is the best method of screening for Developmental Dysplasia of the Hip (DDH) in terms of clinical and cost effectiveness?</li>
    <li class="priority" style="top:679.4px">What are the best strategies to optimise communication of information between patients/carers and clinicians in order to enable shared decision-making?</li>
    <li class="priority" style="top:748.5px">What is the best management for hip displacement in children with Cerebral Palsy?</li>
  </ol>

  <p class="thanks-bar" style="margin:0">Many thanks to all those people who helped us take this work off the ground and helped us finish it!</p>

  <footer class="credits">
    <h2 class="credits__heading">Special thanks to:</h2>
    <ul class="credits__list">
      <li>The Guild of Young Bone Surgeons</li>
      <li>The Northmere Orthopaedic Fellowship</li>
      <li>The Calder Hill University and the</li>
      <li>Harold Vane Collective, who always look for fair play in research!</li>
    </ul>
  </footer>
</main>
</body>
</html>
```